Asian Pakistani: Wedding Invitation

Design a pakistani asian wedding invitation.
Islamic theme, with arabic text:

Text to be used:

Start with: bismillah and dua for marriage. (The Holy Quran chapter 25 verse 75 with arabic text and english translation below)

Mrs. Rubina Sohail wife of (late) Mr. Sohail Imran Qureshi
Cordially requests your company to grace the joyous occasion of the wedding of their beloved daughter
Mehreen Qureshi
Daughter of ( late) Mr Sohail Imran qureshi
with
Bilal Siddiqui
Son of Mr. Junaid Siddiqui & Mrs Shazia Siddiqui

Insha’Allah on Thursday 29th August 2019 at Velvet Orchard
12 Marlow Crescent, Croydon
CR7 2LP
Baraat Arrival 6:30

RSVP
Usman Qureshi 07700 900412
Tariq Mehmood 07700 900583
Faisal Butt 07700 900735

Target Market(s)

Muslims

Font styles to use
Script

Colors

Designer to choose colors to be used in the design.

Requirements
Must have
• stylish calligraphy Arabic lettering of the dua requested above
• Size:
• Long 4" x 9.5"
Nice to have
• ottoman empire: Art theme

```html
<!DOCTYPE html>
<html lang="en">
<head>
<meta charset="utf-8">
<title>Wedding Invitation – Qureshi &amp; Siddiqui</title>
<link rel="stylesheet" href="https://fonts.googleapis.com/css2?family=Great+Vibes&family=Italianno&family=Amiri:wght@400;700&display=swap">
<style>
  :root {
    --stage: #050608;
    --paper: #ffffff;
    --gold: #b8862f;
    --gold-deep: #a0701f;
    --gold-text: #c0933a;
    --gold-light: #f3dd7c;
    --gold-pale: #e8c766;
    --ink: #1b1b1b;
    --ribbon: #d3222a;
    --ribbon-dark: #b5161e;
    --ribbon-light: #ef6a5f;
  }
  * { margin: 0; padding: 0; box-sizing: border-box; }
  html, body { width: 1200px; height: 1054px; overflow: hidden; background: var(--stage); }
  .board { position: relative; width: 1200px; height: 1054px; background: var(--stage); }

  .card {
    position: absolute;
    background: linear-gradient(135deg, var(--gold-light) 0%, var(--gold) 30%, var(--gold-pale) 55%, var(--gold) 80%, var(--gold-light) 100%);
  }
  .card__inner { position: absolute; inset: 13px; background: var(--paper); overflow: hidden; }
  .card__inner--soft { background: linear-gradient(90deg, #fff8ea 0%, var(--paper) 12%, var(--paper) 88%, #fff8ea 100%); }

  .ornament { position: absolute; }
  .ornament--corner {
    background: linear-gradient(135deg, var(--gold) 0%, var(--gold-pale) 100%);
    opacity: .55;
  }
  .ornament--tl { border-radius: 2px 2px 100% 2px; }
  .ornament--tr { border-radius: 2px 2px 2px 100%; }
  .ornament--bl { border-radius: 2px 100% 2px 2px; }
  .ornament--br { border-radius: 100% 2px 2px 2px; }

  /* Tall invitation card */
  .invite { left: 126px; top: 166px; width: 273px; height: 649px; }
  .invite .line {
    position: absolute; left: 0; right: 0; text-align: center;
    font-family: "Great Vibes", cursive; color: var(--gold-text); white-space: nowrap;
    height: 18px; line-height: 18px;
  }
  .bismillah {
    left: 31px; top: 12px; width: 191px; height: 26px;
    background: linear-gradient(90deg, #3a3a3a 0%, #111 50%, #3a3a3a 100%);
    border-radius: 13px; opacity: .85;
  }
  .basmala-en { font-size: 11px; color: #3a3a3a !important; }
  .dua-ar {
    position: absolute; left: 0; right: 0; top: 102px; height: 18px; line-height: 18px; text-align: center;
    font-family: "Amiri", serif; font-size: 10.5px; color: var(--ink); direction: rtl; white-space: nowrap;
  }
  .dua-en {
    position: absolute; left: 6px; right: 6px; top: 124px; text-align: center;
    font-family: "Italianno", cursive; font-size: 10.5px; line-height: 12px; color: #3a3a3a;
  }
  .names { font-size: 13px; }
  .bird {
    background: linear-gradient(135deg, var(--gold-pale) 0%, var(--gold) 100%);
    border-radius: 50% 50% 50% 10%;
  }
  .divider {
    left: 73px; top: 406px; width: 104px; height: 12px;
    background: linear-gradient(90deg, var(--gold-pale), var(--gold), var(--gold-pale));
    border-radius: 6px;
  }
  .details { font-size: 12.5px; }
  .baraat-rule { position: absolute; top: 507px; height: 1px; background: var(--gold); }
  .couple {
    left: 20px; top: 527px; width: 61px; height: 82px;
    background: linear-gradient(180deg, var(--gold-pale) 0%, var(--gold) 100%);
    border-radius: 28px 28px 4px 4px; opacity: .7;
  }
  .rsvp {
    position: absolute; left: 86px; top: 554px;
    font-family: "Great Vibes", cursive; font-size: 10.5px; line-height: 11.7px; color: var(--ink); list-style: none; white-space: nowrap;
  }

  /* Envelope cover card */
  .cover { left: 440px; top: 169px; width: 649px; height: 273px; }
  .cover__title {
    position: absolute; left: 0; right: 0; top: 18px; height: 52px; line-height: 52px; text-align: center;
    font-family: "Great Vibes", cursive; font-weight: 400; font-size: 40px; color: var(--gold-deep); white-space: nowrap;
  }
  .ribbon {
    position: absolute; left: 0; right: 0; top: 105px; height: 22px;
    background: linear-gradient(90deg, var(--ribbon-dark) 0%, var(--ribbon) 18%, var(--ribbon-light) 32%, var(--ribbon) 45%, var(--ribbon) 62%, var(--ribbon-light) 80%, var(--ribbon) 100%);
  }
  .bow {
    left: 263px; top: 83px; width: 99px; height: 82px;
    background: linear-gradient(160deg, var(--ribbon-light) 0%, var(--ribbon) 45%, var(--ribbon-dark) 100%);
    border-radius: 40% 40% 30% 30%;
  }
  .cover__name-line { position: absolute; left: 148px; width: 327px; top: 217px; height: 1px; background: var(--gold); }
</style>
</head>
<body>
<main class="board">

  <article class="card invite" aria-label="Wedding invitation card">
    <div class="card__inner card__inner--soft">
      <div class="ornament ornament--corner ornament--tl" style="left:2px;top:4px;width:38px;height:39px" role="img" aria-label="Gold filigree corner ornament"></div>
      <div class="ornament ornament--corner ornament--tr" style="right:2px;top:4px;width:38px;height:39px" role="img" aria-label="Gold filigree corner ornament"></div>
      <div class="ornament ornament--corner ornament--bl" style="left:2px;top:580px;width:38px;height:39px" role="img" aria-label="Gold filigree corner ornament"></div>
      <div class="ornament ornament--corner ornament--br" style="right:2px;top:580px;width:38px;height:39px" role="img" aria-label="Gold filigree corner ornament"></div>

      <div class="ornament bismillah" role="img" aria-label="Bismillah in Arabic calligraphy"></div>
      <p class="line basmala-en" style="top:51px">In the name of Allah, the most Gracious, most Merciful</p>

      <p class="dua-ar">رَبَّنَا هَبْ لَنَا مِنْ أَزْوَاجِنَا وَذُرِّيَّاتِنَا قُرَّةَ أَعْيُنٍ وَاجْعَلْنَا لِلْمُتَّقِينَ إِمَامًا</p>
      <p class="dua-en">Our Lord, grant us of our wives and children the delight of our eyes, and make us<br>a model of the righteous (Sura Al Furqan:75)</p>

      <div class="ornament bird" style="left:10px;top:150px;width:40px;height:38px" role="img" aria-label="Gold dove in flight"></div>
      <div class="ornament bird" style="left:203px;top:184px;width:36px;height:36px" role="img" aria-label="Gold dove in flight"></div>

      <p class="line names" style="top:183px">Mrs. Rubina Sohail wife of (late)</p>
      <p class="line names" style="top:205px">Mr. Sohail Imran Qureshi</p>
      <p class="line names" style="top:228px">Cordially requests your company to grace the joyous</p>
      <p class="line names" style="top:251px">occasion of &nbsp;the wedding of their beloved daughter</p>
      <p class="line names" style="top:272px">Mehreen Qureshi</p>
      <p class="line names" style="top:295px">Daughter of (late) Mr Sohail Imran qureshi</p>
      <p class="line names" style="top:317px">with</p>
      <p class="line names" style="top:339px">Bilal Siddiqui</p>
      <p class="line names" style="top:362px;font-size:12.5px">Son of Mr. Junaid Siddiqui &amp; Mrs Shazia Siddiqui</p>

      <div class="ornament divider" role="img" aria-label="Gold scroll divider ornament"></div>

      <p class="line details" style="top:436px">Insha’Allah on Thursday 29th August 2019 at</p>
      <p class="line details" style="top:457px">Velvet Orchard 12 Marlow Crescent, Croydon</p>
      <p class="line details" style="top:476px">CR7 2LP</p>
      <span class="baraat-rule" style="left:40px;width:36px"></span>
      <p class="line details" style="top:497px">Baraat Arrival 6:30</p>
      <span class="baraat-rule" style="left:173px;width:35px"></span>

      <div class="ornament couple" role="img" aria-label="Gold line illustration of bride and groom"></div>

      <ul class="rsvp">
        <li>RSVP</li>
        <li>Usman Qureshi 07700 900412</li>
        <li>Tariq Mehmood 07700 900583</li>
        <li>Faisal Butt 07700 900735</li>
      </ul>
    </div>
  </article>

  <article class="card cover" aria-label="Wedding invitation envelope cover">
    <div class="card__inner">
      <div class="ornament ornament--corner ornament--tl" style="left:5px;top:3px;width:79px;height:77px" role="img" aria-label="Gold filigree corner ornament"></div>
      <div class="ornament ornament--corner ornament--tr" style="right:5px;top:3px;width:79px;height:77px" role="img" aria-label="Gold filigree corner ornament"></div>
      <div class="ornament ornament--corner ornament--bl" style="left:5px;top:165px;width:79px;height:79px" role="img" aria-label="Gold filigree corner ornament"></div>
      <div class="ornament ornament--corner ornament--br" style="right:5px;top:165px;width:79px;height:79px" role="img" aria-label="Gold filigree corner ornament"></div>

      <h1 class="cover__title">Wedding Invitation</h1>
      <div class="ribbon"></div>
      <div class="ornament bow" role="img" aria-label="Red satin ribbon bow"></div>
      <span class="cover__name-line"></span>
    </div>
  </article>

</main>
</body>
</html>
```